Vodka Soda brand identity design and label design

New vodka soda (hard seltzer) brand needs a brand identity design and label designs.

The brand name is VELMO

We produce vodka soda packaged in cans. They come in three flavours
- Raspberry and Lime
- Pina Colada
- Black Cherry

We would like to have the designs look similar (same template) but have one difference depending on the fruit flavour.

The final delivered package should contain
- brand identity design guide with a logo, font and colour schemes
- 3 label designs on the same template (label size 8.125 x 5 inches)

Some example designs of similar products are attached to the project.

Target Market(s)

Gender neutral, younger population

Colors
000000

Requirements
Must have
• Bright background and bright eye catching colours.

```html
<!DOCTYPE html>
<html lang="en">
<head>
<meta charset="utf-8">
<title>VELMO Hard Seltzer – Raspberry Lime Label</title>
<link rel="stylesheet" href="https://fonts.googleapis.com/css2?family=Lato:wght@700&family=Montserrat:wght@300;500&display=swap">
<style>
  :root {
    --stage: #2890b0;
    --can-deep: #134a66;
    --can-mid: #1d6f95;
    --can-bright: #2fa6d2;
    --band-white: #eef2f4;
    --band-shade: #c9d1d6;
    --seltzer-cyan: #25b3dd;
    --wordmark: #dfe4e8;
    --flavour-red: #7a1d24;
    --berry-red: #d8452a;
    --berry-dark: #a52a1c;
    --leaf-green: #5e9a34;
    --lime-green: #6f9a24;
    --lime-dark: #44661a;
  }
  html, body {
    margin: 0;
    width: 1200px;
    height: 1200px;
    overflow: hidden;
    background: var(--stage);
  }
  .stage {
    width: 1200px;
    height: 1200px;
    display: flex;
    align-items: center;
    justify-content: center;
  }
  .label {
    width: 560px;
    height: 1040px;
    display: block;
  }
  .seltzer-text {
    font-family: "Lato", sans-serif;
    font-weight: 700;
    font-size: 34px;
    letter-spacing: 4px;
    fill: var(--seltzer-cyan);
  }
  .brand-name {
    font-family: "Montserrat", sans-serif;
    font-weight: 500;
    font-size: 178px;
    letter-spacing: 14px;
    fill: var(--wordmark);
  }
  .flavour-name {
    font-family: "Montserrat", sans-serif;
    font-weight: 300;
    font-size: 44px;
    letter-spacing: 3px;
    fill: var(--flavour-red);
  }
</style>
</head>
<body>
<main class="stage">
  <svg class="label" viewBox="0 0 560 1040" xmlns="http://www.w3.org/2000/svg">
    <defs>
      <linearGradient id="metal-blue" x1="0" y1="0" x2="1" y2="0">
        <stop offset="0" stop-color="var(--can-mid)"/>
        <stop offset="0.3" stop-color="var(--can-bright)"/>
        <stop offset="0.55" stop-color="var(--can-mid)"/>
        <stop offset="1" stop-color="var(--can-deep)"/>
      </linearGradient>
      <linearGradient id="white-band" x1="0" y1="0" x2="1" y2="0">
        <stop offset="0" stop-color="var(--band-shade)"/>
        <stop offset="0.5" stop-color="var(--band-white)"/>
        <stop offset="1" stop-color="var(--band-shade)"/>
      </linearGradient>
      <linearGradient id="berry-tones" x1="0" y1="0" x2="0" y2="1">
        <stop offset="0" stop-color="var(--berry-dark)"/>
        <stop offset="0.55" stop-color="var(--berry-red)"/>
        <stop offset="1" stop-color="var(--leaf-green)"/>
      </linearGradient>
      <linearGradient id="lime-tones" x1="0" y1="0" x2="0" y2="1">
        <stop offset="0" stop-color="var(--lime-green)"/>
        <stop offset="1" stop-color="var(--lime-dark)"/>
      </linearGradient>
    </defs>

    <rect class="label-body" x="0" y="0" width="560" height="1040" fill="url(#metal-blue)"/>
    <rect class="side-band" x="70" y="0" width="54" height="1040" fill="url(#white-band)"/>

    <path class="raspberry-cluster" role="img" aria-label="Raspberries with leaves across the top of the label"
          d="M0 0 H560 V230 Q500 300 440 250 Q380 330 330 230 Q260 270 200 190 Q130 210 80 170 Q40 200 0 180 Z"
          fill="url(#berry-tones)"/>

    <text class="seltzer-text" transform="translate(190 640) rotate(-90)">HARD SELTZER</text>
    <text class="brand-name" transform="translate(390 740) rotate(-90)">VELMO</text>

    <text class="flavour-name" x="180" y="820">Raspberry</text>
    <text class="flavour-name" x="180" y="872">Lime</text>

    <path class="lime-cluster" role="img" aria-label="Whole limes along the bottom of the label"
          d="M0 940 Q60 900 120 930 Q190 890 260 935 Q340 895 420 930 Q490 900 560 925 V1040 H0 Z"
          fill="url(#lime-tones)"/>
  </svg>
</main>
</body>
</html>
```